こんにちは、

森川建設の森川です!

弊社は、
八王子市で足場屋を営んでおります!

筋トレ大好きな若者向けの求人用のチラシを作ってもらいたいです。

アルバイト募集って感じで、

・ロングタイム
8:00〜17:00で1日16,000円

・ショートタイム
10:00〜16:00で1日13,000円

置き場などでの残業はありません。

筋肉、体幹を、鍛えて、
かつ、

ワンチャン技術も身につく!

※筋トレ好きや、格闘家や、アスリートに最適!

-----------------------------
弊社の売り(ここは、入れないほうが良ければ入れなくてもいいです!参考までに)

・会社の理念が、社員満足度を第一にして、会社と、関わる全ての人を潤わす。
・質の高い足場屋さん。技術力も優れている。
・週休2日制
・自分の用事に合わせて好きな日に休める。
・関わる全ての人が 経済的、精神的、時間的に潤うことを目指している。
・チームワークを大事にしている。
・全スタッフ14名
・イベント多数 (毎年海外旅行or国内旅行+レジャー)
・ホームページ morikawakensetsu.info

こんな感じなのですが、これを、イメージしてもらい、見る人に、インパクトと高感度を与えてくれて、口コミや、実際に応募がきたら嬉しいです。

㍿森川建設
A5
片面
シンプル 複雑
単色 カラフル
暗い 明るい
日常 高級
遊び心 厳粛
未来的 伝統的
女性的 男性的
一応会社のイメージカラーは、紺ですが、色は、オススメの色でお願いしたいです!
• 高解像度JPG (.jpg)
• イラストレーター形式 (.ai)
・バス広告のロゴで、バイアスを構築していますので、バス広告のデザインを利用して作っていただけると相乗効果を生むことができるので、お願いしたいです!

あ、このロゴなんか見たことあるのような感じです!
※ですが、上のロゴを入れるのが、あまり良くないと思えば、それは、気にしなくても良いです!1番は、若者を入れたいので、そのためを重視してもらいたいです!

・納品ですが、金額や、条件を少し編集できるようにしたいので、アウトライン化してるものと、されてないものを納品して頂きたいです!
A4でもA6でも使えるようにしたいです!
社内で話し合ったところ、もう少しインパクトの強い印象に残るものができるんじゃ無いかという期待を込めて延長させてもらいました。

・筋肉(鍛えられる)、
・短時間制のアルバイトがある(短時間制の職人系のアルバイトでは、珍しいです。)
・ロングタイムも、選べる。

これが1番伝えたい内容です。

次に、
職人さんは、いまとても減ってきてるので、希少性がかなり高くなっています。先に技術を学んでおくことで、後にブルーオーシャンになるのでは無いか?と予測しています。

これは、僕の伝えたい思い出もありますが、
チラシとして何を目的にしてるかは、
人を入れたいという事が目的なので、

ユーザー側の気持ちになってもらい、

・身体に自信がある人や
・身体にコンプレックスを持っていてムキムキになりたいと考えてる人
・頭を使うよりも身体を動かす事が自分に向いていると感じてる人に

響くような、チラシになることを願っています。

1発で目に引かれて、頭から離れないような、チラシにしてもらいたいです!

よろしくお願いします。

インパクトもあり、なんとなく清潔にも感じて、無駄な主張もなくシンプルで良い作品だと感じました。

多くの素晴らしい作品があり、選定するのにとても困りました。

本当にありがとうございます。

職人の価値向上を目指して、頑張ります!

本当にありがとうございました。

これからも宜しくお願い致します。

```html
<!DOCTYPE html>
<html lang="ja">
<head>
<meta charset="utf-8">
<title>足場工事スタッフ募集｜株式会社森川建設</title>
<link rel="stylesheet" href="https://fonts.googleapis.com/css2?family=Noto+Sans+JP:wght@500;700;900&display=swap">
<style>
:root{
  --navy:#0f2a66;
  --navy-deep:#0a1d4a;
  --blue:#1d4fb8;
  --red:#d8261c;
  --white:#ffffff;
  --ink:#13203d;
  --sky-top:#5f7fa8;
  --sky-bottom:#cfd9e6;
}
*{margin:0;padding:0;box-sizing:border-box}
html,body{width:844px;height:1200px;overflow:hidden;background:#fff}
body{font-family:"Noto Sans JP",sans-serif;color:var(--ink)}
.flyer{position:relative;width:844px;height:1200px;overflow:hidden;background:#fff}
.backdrop{position:absolute;left:0;top:0;width:844px;height:1010px;
  background:linear-gradient(180deg,#1a2c55 0%,var(--sky-top) 22%,#a9bcd3 55%,var(--sky-bottom) 100%)}
.worker-photo{position:absolute;right:0;top:0;width:440px;height:470px;
  background:linear-gradient(200deg,#8aa3c2 0%,#4d6486 55%,#2a3c5e 100%);opacity:.9}
.lead{position:absolute;left:26px;color:var(--white);font-weight:900;font-size:33px;letter-spacing:1px;white-space:nowrap;
  text-shadow:0 0 3px var(--navy-deep),0 0 3px var(--navy-deep),2px 2px 0 var(--navy-deep)}
.lead.one{top:14px}
.lead.two{top:62px}
.headline-box{position:absolute;left:28px;top:150px;width:580px;height:170px;background:var(--navy);
  display:flex;align-items:center;justify-content:center}
.headline-box span{color:var(--white);font-weight:900;font-size:150px;line-height:1;letter-spacing:40px;margin-right:-40px}
.headline-sub{position:absolute;left:28px;top:328px;color:var(--navy);font-weight:900;font-size:78px;letter-spacing:2px;line-height:1.05;white-space:nowrap;
  text-shadow:0 0 4px #fff,0 0 4px #fff,0 0 4px #fff,0 0 4px #fff}
.shift-band{position:absolute;left:28px;width:530px;height:48px;background:var(--navy);color:var(--white);
  font-weight:900;font-size:32px;display:flex;align-items:center;padding-left:16px;letter-spacing:1px;white-space:nowrap}
.shift-band.long{top:425px}
.shift-band.short{top:584px}
.wage{position:absolute;left:28px;height:96px;display:flex;align-items:baseline;color:var(--navy);font-weight:900;line-height:1;white-space:nowrap;
  text-shadow:0 0 4px #fff,0 0 4px #fff,0 0 4px #fff,0 0 4px #fff}
.wage .label{font-size:62px}
.wage .amount{font-size:92px;letter-spacing:-1px}
.wage .unit{font-size:62px}
.wage.long{top:480px}
.wage.short{top:639px}
.perk{position:absolute;left:594px;width:224px;background:var(--navy);color:var(--white);font-weight:900;
  text-align:center;display:flex;align-items:center;justify-content:center;line-height:1.4;padding:0 4px;white-space:nowrap}
.perk.days{top:484px;height:58px;font-size:26px}
.perk.overtime{top:558px;height:78px;font-size:23px}
.perk.holiday{top:652px;height:80px;font-size:20px}
.either-box{position:absolute;left:28px;top:754px;width:270px;height:72px;background:var(--blue);color:var(--white);
  font-weight:900;font-size:22px;line-height:1.35;text-align:center;display:flex;align-items:center;justify-content:center;
  border:3px solid var(--white);white-space:nowrap}
.philosophy{position:absolute;left:28px;top:842px;color:var(--white);font-weight:900;font-size:25px;line-height:1.45;white-space:nowrap;
  text-shadow:0 0 3px var(--navy-deep),0 0 3px var(--navy-deep),0 0 3px var(--navy-deep),2px 2px 0 var(--navy-deep)}
.appeal-list{position:absolute;left:340px;top:754px;width:478px;list-style:none}
.appeal-list li{display:flex;align-items:center;gap:10px;height:44px;margin-bottom:8px;background:var(--white);
  padding:0 12px;font-weight:700;font-size:20px;color:var(--ink);border:2px solid var(--navy);white-space:nowrap}
.appeal-list li.two-line{height:64px;font-size:18px;line-height:1.35}
.appeal-list svg{flex:0 0 22px}
.footer{position:absolute;left:0;top:1010px;width:844px;height:190px;background:var(--white);border-top:6px solid var(--navy)}
.brand{position:absolute;left:26px;top:22px;display:flex;align-items:center;gap:14px}
.brand-mark{width:72px;height:72px;background:var(--navy)}
.brand-roman{font-size:17px;font-weight:500;color:var(--navy);letter-spacing:1px}
.brand-name{font-size:40px;font-weight:900;color:var(--navy);line-height:1.1}
.address{position:absolute;left:520px;top:30px;font-size:16px;font-weight:500;color:var(--ink);line-height:1.5}
.contact{position:absolute;left:26px;top:112px;display:flex;align-items:center;gap:18px}
.tel{display:flex;align-items:center;gap:10px;background:var(--red);color:var(--white);font-weight:900;padding:6px 18px;height:62px}
.tel .tag{font-size:30px}
.tel .num{font-size:46px;letter-spacing:1px}
.fax{display:flex;align-items:center;gap:8px;font-weight:900;color:var(--navy)}
.fax .tag{background:var(--navy);color:var(--white);font-size:22px;padding:2px 8px}
.fax .num{font-size:30px}
</style>
</head>
<body>
<div class="flyer">
  <div class="backdrop" role="img" aria-label="背景写真：青空の下に組まれた建設現場の足場"></div>
  <div class="worker-photo" role="img" aria-label="写真：ヘルメットをかぶり笑顔で立つ足場職人"></div>

  <p class="lead one">ガッツリ稼いでプライベートを充実させたい人</p>
  <p class="lead two">身体を動かすのが好きな人・鍛えたい人</p>

  <div class="headline-box"><span>足場</span></div>
  <h1 class="headline-sub">工事スタッフ募集</h1>

  <div class="shift-band long">ロングタイム 8:00～17:00</div>
  <p class="wage long"><span class="label">日給</span><span class="amount">16,000</span><span class="unit">円</span></p>

  <div class="shift-band short">ショートタイム 10:00～16:00</div>
  <p class="wage short"><span class="label">日給</span><span class="amount">13,000</span><span class="unit">円</span></p>

  <div class="perk days">週休２日制</div>
  <div class="perk overtime">置き場などでの<br>残業なし</div>
  <div class="perk holiday">自分の用事に合わせて<br>好きな日に休めます</div>

  <div class="either-box">ショート・ロングタイム<br>どちらでも可</div>
  <p class="philosophy">関わる全ての人が<br>潤うことを目指しています</p>

  <ul class="appeal-list">
    <li><svg width="22" height="22" viewBox="0 0 24 24"><path d="M3 12l6 6L21 5" fill="none" stroke="#d8261c" stroke-width="4" stroke-linecap="round" stroke-linejoin="round"/></svg>技術力に優れた質の高い足場屋です</li>
    <li><svg width="22" height="22" viewBox="0 0 24 24"><path d="M3 12l6 6L21 5" fill="none" stroke="#d8261c" stroke-width="4" stroke-linecap="round" stroke-linejoin="round"/></svg>チームワークを大事にしています</li>
    <li><svg width="22" height="22" viewBox="0 0 24 24"><path d="M3 12l6 6L21 5" fill="none" stroke="#d8261c" stroke-width="4" stroke-linecap="round" stroke-linejoin="round"/></svg>身体も鍛えられ技術も身に付きます</li>
    <li class="two-line"><svg width="22" height="22" viewBox="0 0 24 24"><path d="M3 12l6 6L21 5" fill="none" stroke="#d8261c" stroke-width="4" stroke-linecap="round" stroke-linejoin="round"/></svg><span>イベント多数あり、充実しています<br>（毎年海外旅行or国内旅行+レジャー）</span></li>
  </ul>

  <footer class="footer">
    <div class="brand">
      <div class="brand-mark"></div>
      <div>
        <p class="brand-roman">morikawa.corporation</p>
        <p class="brand-name">株式会社森川建設</p>
      </div>
    </div>
    <p class="address">〒192-0000<br>東京都八王子市緑町12-5 森川ビル1階</p>
    <div class="contact">
      <div class="tel">
        <svg width="34" height="34" viewBox="0 0 24 24"><path d="M6.6 10.8a15 15 0 006.6 6.6l2.2-2.2a1 1 0 011-.25 11.4 11.4 0 003.6.57 1 1 0 011 1V20a1 1 0 01-1 1A17 17 0 013 4a1 1 0 011-1h3.5a1 1 0 011 1c0 1.25.2 2.45.57 3.570a1 1 0 01-.25 1z" fill="#fff"/></svg>
        <span class="tag">TEL</span><span class="num">042-612-4870</span>
      </div>
      <div class="fax"><span class="tag">FAX</span><span class="num">042-612-4871</span></div>
    </div>
  </footer>
</div>
</body>
</html>
```